Poster for our office

Looking to get a large print or poster for our office. That has our logo; our core mission; and examples of feedback from clients all on the one print.
Is this something you do?
If so, you’ll see most of the content on our website: pmrd.com.au

```html
<!DOCTYPE html>
<html lang="en">
<head>
<meta charset="utf-8">
<title>PMRD Leadership Forum — Poster</title>
<link rel="stylesheet" href="https://fonts.googleapis.com/css2?family=Playfair+Display:ital,wght@0,400;0,700;1,400&family=Jost:wght@400&display=swap">
<style>
  :root {
    --ink: #080808;
    --ink-warm: #2a2520;
    --white: #ffffff;
    --gold: #c9a96e;
    --gold-soft: rgba(201, 169, 110, 0.75);
  }
  * { margin: 0; padding: 0; box-sizing: border-box; }
  html, body { width: 848px; height: 1200px; overflow: hidden; background: var(--ink); }
  .poster {
    position: relative;
    width: 848px;
    height: 1200px;
    overflow: hidden;
    font-family: "Playfair Display", Georgia, serif;
    color: var(--white);
  }
  .backdrop {
    position: absolute;
    inset: 0;
    background: linear-gradient(160deg, var(--ink) 0%, var(--ink) 55%, var(--ink-warm) 100%);
  }
  .brand {
    position: absolute;
    left: 64px;
    top: 84px;
    font-size: 34px;
    font-weight: 400;
    letter-spacing: 0.01em;
  }
  .mission {
    position: absolute;
    left: 64px;
    top: 200px;
    font-size: 56px;
    line-height: 69.5px;
    font-weight: 400;
    white-space: nowrap;
  }
  .mission .highlight { color: var(--gold); font-weight: 700; }
  .section-label {
    position: absolute;
    left: 64px;
    top: 612px;
    display: flex;
    align-items: center;
    gap: 15px;
    font-family: "Jost", Arial, sans-serif;
    font-size: 14px;
    font-weight: 400;
    letter-spacing: 0.34em;
  }
  .section-label::before {
    content: "";
    width: 42px;
    height: 1px;
    background: var(--gold);
  }
  .testimonials {
    position: absolute;
    left: 0;
    top: 681px;
    width: 848px;
    height: 323px;
  }
  .testimonial {
    position: absolute;
    top: 0;
    height: 323px;
  }
  .testimonial + .testimonial { border-left: 1px solid var(--gold-soft); }
  .testimonial:nth-child(1) { left: 64px; width: 217px; }
  .testimonial:nth-child(2) { left: 281px; width: 251px; padding-left: 24px; }
  .testimonial:nth-child(3) { left: 532px; width: 260px; padding-left: 23px; }
  .quote-mark {
    display: block;
    height: 44px;
    margin-top: 4px;
    font-size: 80px;
    line-height: 80px;
    font-weight: 700;
    color: var(--gold);
    overflow: hidden;
  }
  .quote-text {
    margin-top: 2px;
    font-style: italic;
    font-size: 19.5px;
    line-height: 29.8px;
    height: 226px;
    white-space: nowrap;
  }
  .quote-rule {
    width: 21px;
    height: 1px;
    background: var(--gold);
  }
  .quote-source {
    margin-top: 14px;
    font-family: "Jost", Arial, sans-serif;
    font-size: 12px;
    letter-spacing: 0.22em;
  }
  .web-address {
    position: absolute;
    left: 64px;
    top: 1094px;
    font-size: 28px;
    letter-spacing: 0.08em;
    color: var(--gold);
  }
</style>
</head>
<body>
<main class="poster">
  <div class="backdrop" role="img" aria-label="Dark interior with warm light falling across a wall and floor"></div>

  <header class="brand">PMRD Leadership Forum</header>

  <h1 class="mission">
    Supporting<br>
    <span class="highlight">public sector leaders</span><br>
    to think clearly,<br>
    perform at their best and<br>
    deliver better outcomes.
  </h1>

  <h2 class="section-label">WHAT PARTICIPANTS SAY</h2>

  <section class="testimonials">
    <blockquote class="testimonial">
      <span class="quote-mark">“</span>
      <p class="quote-text">The best professional<br>development I have<br>undertaken in 30 years<br>of public service. It has<br>changed the way I think<br>about my role and my<br>leadership.”</p>
      <div class="quote-rule"></div>
      <p class="quote-source">Participant feedback</p>
    </blockquote>
    <blockquote class="testimonial">
      <span class="quote-mark">“</span>
      <p class="quote-text">What struck me most<br>was the calibre of the<br>people in the room. These<br>were leaders I respected<br>enormously — and they<br>were wrestling with the<br>same things I was.”</p>
      <div class="quote-rule"></div>
      <p class="quote-source">Participant feedback</p>
    </blockquote>
    <blockquote class="testimonial">
      <span class="quote-mark">“</span>
      <p class="quote-text">I have done a lot of<br>leadership development<br>over the years. Nothing<br>has come close to this<br>in terms of practical<br>value and immediate<br>application to my work.”</p>
      <div class="quote-rule"></div>
      <p class="quote-source">Participant feedback</p>
    </blockquote>
  </section>

  <footer class="web-address">pmrd.com.au</footer>
</main>
</body>
</html>
```